New Company Business Card design

Looking for a corporate looking business card utilising my new logo design - the logo i would like embossed as one option and flat as another - simplistic but stylish - less is more - we are an import export business launching into the market - i would like a couple of options as main background - Grey or Black

```html
<!DOCTYPE html>
<html lang="en">
<head>
<meta charset="utf-8">
<title>Meridian Trade Partners – Business Card Options</title>
<link rel="stylesheet" href="https://fonts.googleapis.com/css2?family=Crimson+Text:wght@400;600&display=swap">
<style>
  :root{
    --page:#ffffff;
    --charcoal:#333333;
    --mist:#d9d9d9;
    --band:#9a9a9a;
    --brand-blue:#1474bf;
    --ink:#1e1e1e;
    --light-ink:#f2f2f2;
    --icon-grey:#6b6b6b;
  }
  *{box-sizing:border-box;margin:0;padding:0}
  html,body{width:1200px;height:1200px;overflow:hidden;background:var(--page)}
  .sheet{position:relative;width:1500px;height:1500px;transform:scale(.8);transform-origin:0 0;font-family:"Crimson Text",Georgia,serif}
  .card{position:absolute;width:712px;height:425px;border-radius:22px;overflow:hidden}
  .card--front-dark{left:26px;top:114px;background:var(--mist)}
  .card--back-dark{left:758px;top:114px;background:var(--charcoal)}
  .card--front-grey{left:26px;top:838px;background:var(--mist);border:1px solid #c4c4c4}
  .card--back-grey{left:758px;top:838px;background:var(--mist);border:1px solid #c4c4c4}
  .card__art{position:absolute;inset:0;width:712px;height:425px}
  .brand{position:absolute;display:flex;align-items:center;gap:10px;color:var(--brand-blue);font-weight:600;font-size:28px;line-height:1;letter-spacing:.5px;white-space:nowrap}
  .brand__dot{width:22px;height:22px;border-radius:50%;background:var(--brand-blue);flex:none}
  .card--front-dark .brand,.card--front-grey .brand{left:52px;top:150px}
  .card--back-dark .brand,.card--back-grey .brand{left:0;right:0;top:204px;justify-content:center}
  .contacts{position:absolute;right:22px;top:196px;list-style:none}
  .contacts li{display:flex;align-items:center;justify-content:flex-end;height:36px;margin-bottom:22px;font-size:25px;color:var(--ink)}
  .contacts li:nth-child(3){margin-bottom:18px}
  .contacts svg{margin-left:14px;flex:none}
  .holder{position:absolute;left:27px;top:340px;display:flex;align-items:center;gap:16px;font-size:29px;color:var(--ink);white-space:nowrap}
  .tagline{position:absolute;left:0;right:0;top:336px;text-align:center;font-size:36px}
  .card--back-dark .tagline{color:var(--light-ink)}
  .card--back-grey .tagline{color:var(--ink)}
</style>
</head>
<body>
<main class="sheet">

  <section class="card card--front-dark">
    <svg class="card__art" viewBox="0 0 712 425" aria-hidden="true">
      <path d="M0 0H712V128C610 70 520 100 440 180C350 270 290 305 200 305C120 305 50 260 0 212Z" fill="var(--band)"/>
      <path d="M0 0H712V75C610 72 520 100 430 185C340 265 280 292 200 290C120 288 40 240 0 188Z" fill="var(--charcoal)"/>
    </svg>
    <div class="brand"><span class="brand__dot"></span>Meridian Trade Partners</div>
    <ul class="contacts">
      <li>++ 555 210<svg width="34" height="34" viewBox="0 0 34 34"><circle cx="17" cy="17" r="15" fill="none" stroke="var(--brand-blue)" stroke-width="2"/><path d="M12 9c-2 1-3 3-2 6 1 4 5 8 9 10 3 1 5 0 6-2l-3-3-2 1c-2-1-4-3-5-5l1-2z" fill="none" stroke="var(--brand-blue)" stroke-width="2" stroke-linejoin="round"/></svg></li>
      <li>++ 555 314<svg width="34" height="34" viewBox="0 0 34 34"><circle cx="17" cy="17" r="15" fill="none" stroke="var(--brand-blue)" stroke-width="2"/><path d="M12 9c-2 1-3 3-2 6 1 4 5 8 9 10 3 1 5 0 6-2l-3-3-2 1c-2-1-4-3-5-5l1-2z" fill="none" stroke="var(--brand-blue)" stroke-width="2" stroke-linejoin="round"/></svg></li>
      <li>meridiantp.com<svg width="52" height="38" viewBox="0 0 52 38"><rect x="1" y="2" width="50" height="22" rx="4" fill="none" stroke="var(--brand-blue)" stroke-width="2"/><text x="26" y="18" font-size="11" font-family="Arial,sans-serif" font-weight="700" fill="var(--brand-blue)" text-anchor="middle">www://</text><path d="M32 20l12 6-5 1 4 6-2 1-4-6-3 4z" fill="var(--brand-blue)"/></svg></li>
      <li>ar@meridiantp.com<svg width="32" height="22" viewBox="0 0 32 22"><rect width="32" height="22" fill="var(--brand-blue)"/><path d="M1 1l15 11L31 1M1 21l11-10M31 21L20 11" stroke="#fff" stroke-width="1.6" fill="none"/></svg></li>
    </ul>
    <div class="holder"><svg width="66" height="66" viewBox="0 0 66 66"><circle cx="33" cy="33" r="31" fill="none" stroke="var(--icon-grey)" stroke-width="2.5"/><path d="M33 14c-7 0-11 5-11 12 0 5 3 9 5 11v4c-8 2-14 5-16 10M33 14c7 0 11 5 11 12 0 5-3 9-5 11v4c8 2 14 5 16 10" fill="none" stroke="var(--icon-grey)" stroke-width="2.5"/></svg>Mr. Alan Reyes, Director</div>
  </section>

  <section class="card card--back-dark">
    <div class="brand"><span class="brand__dot"></span>Meridian Trade Partners</div>
    <p class="tagline">Import Export Business Launching</p>
  </section>

  <section class="card card--front-grey">
    <svg class="card__art" viewBox="0 0 712 425" aria-hidden="true">
      <path d="M430 162C500 100 600 70 712 78V128C640 90 530 88 430 162Z" fill="var(--brand-blue)"/>
      <path d="M0 190C60 260 180 310 290 268C190 295 80 270 0 240Z" fill="var(--brand-blue)"/>
    </svg>
    <div class="brand"><span class="brand__dot"></span>Meridian Trade Partners</div>
    <ul class="contacts">
      <li>++ 555 210<svg width="34" height="34" viewBox="0 0 34 34"><circle cx="17" cy="17" r="15" fill="none" stroke="var(--brand-blue)" stroke-width="2"/><path d="M12 9c-2 1-3 3-2 6 1 4 5 8 9 10 3 1 5 0 6-2l-3-3-2 1c-2-1-4-3-5-5l1-2z" fill="none" stroke="var(--brand-blue)" stroke-width="2" stroke-linejoin="round"/></svg></li>
      <li>++ 555 314<svg width="34" height="34" viewBox="0 0 34 34"><circle cx="17" cy="17" r="15" fill="none" stroke="var(--brand-blue)" stroke-width="2"/><path d="M12 9c-2 1-3 3-2 6 1 4 5 8 9 10 3 1 5 0 6-2l-3-3-2 1c-2-1-4-3-5-5l1-2z" fill="none" stroke="var(--brand-blue)" stroke-width="2" stroke-linejoin="round"/></svg></li>
      <li>meridiantp.com<svg width="52" height="38" viewBox="0 0 52 38"><rect x="1" y="2" width="50" height="22" rx="4" fill="none" stroke="var(--brand-blue)" stroke-width="2"/><text x="26" y="18" font-size="11" font-family="Arial,sans-serif" font-weight="700" fill="var(--brand-blue)" text-anchor="middle">www://</text><path d="M32 20l12 6-5 1 4 6-2 1-4-6-3 4z" fill="var(--brand-blue)"/></svg></li>
      <li>ar@meridiantp.com<svg width="32" height="22" viewBox="0 0 32 22"><rect width="32" height="22" fill="var(--brand-blue)"/><path d="M1 1l15 11L31 1M1 21l11-10M31 21L20 11" stroke="#fff" stroke-width="1.6" fill="none"/></svg></li>
    </ul>
    <div class="holder"><svg width="66" height="66" viewBox="0 0 66 66"><circle cx="33" cy="33" r="31" fill="none" stroke="var(--ink)" stroke-width="2.5"/><path d="M33 14c-7 0-11 5-11 12 0 5 3 9 5 11v4c-8 2-14 5-16 10M33 14c7 0 11 5 11 12 0 5-3 9-5 11v4c8 2 14 5 16 10" fill="none" stroke="var(--ink)" stroke-width="2.5"/></svg>Mr. Alan Reyes, Director</div>
  </section>

  <section class="card card--back-grey">
    <div class="brand"><span class="brand__dot"></span>Meridian Trade Partners</div>
    <p class="tagline">Import Export Business Launching</p>
  </section>

</main>
</body>
</html>
```